Premium modern eliquids labels 84.5 x 80 mm

I am looking for modern graphics for the labels of a new eliquid line that will have 4 different types of eliquids. It will have a tobacco one (brown colours maybe), a fruity one (bright colours maybe), a minty one (green colours maybe) and a creamy one (beige colours maybe).
I will need one of them to see how the design is, that design will have to be adapted to the other 3 colours of the label.
The brand logo is attached. I also attached a sample of what is mandatory to write on the label, you can change size, place and font of what is written, the only thing that cannot be reduced is the yellow parts. I attach the bottle that we will use.The size of the label is 84.5 x 80 mm (base x height).

Target Market(s)

vapers

Requirements
Must have
• My project must have one of the labels.

```html
<!DOCTYPE html>
<html lang="en">
<head>
<meta charset="utf-8">
<title>Lumen Drift – Eliquid Label Range</title>
<link rel="stylesheet" href="https://fonts.googleapis.com/css2?family=Antonio:wght@400;600&family=Pathway+Gothic+One&display=swap">
<style>
  :root {
    --backdrop: #e8e6e7;
    --label-black: #050505;
    --brand-blue: #6bbde3;
    --text-white: #ffffff;
    --tobacco-light: #e9a042;
    --tobacco-dark: #c2560d;
    --fruity-light: #f7b0a4;
    --fruity-dark: #f2705f;
    --minty-light: #7cd491;
    --minty-dark: #2fb25a;
    --creamy-light: #fff3cf;
    --creamy-dark: #f4dfa3;
  }
  * { margin: 0; padding: 0; box-sizing: border-box; }
  html, body {
    width: 1200px;
    height: 1137px;
    overflow: hidden;
    background: var(--backdrop);
  }
  .range {
    position: relative;
    width: 1200px;
    height: 1137px;
  }
  .label {
    position: absolute;
    top: 444px;
    width: 196px;
    height: 520px;
    background: var(--label-black);
    overflow: hidden;
    text-align: center;
  }
  .label--tobacco { left: 133px; --accent-light: var(--tobacco-light); --accent-dark: var(--tobacco-dark); }
  .label--fruity  { left: 377px; --accent-light: var(--fruity-light);  --accent-dark: var(--fruity-dark); }
  .label--minty   { left: 621px; --accent-light: var(--minty-light);   --accent-dark: var(--minty-dark); }
  .label--creamy  { left: 865px; --accent-light: var(--creamy-light);  --accent-dark: var(--creamy-dark); }

  .brand-name {
    position: absolute;
    top: 92px;
    left: 0;
    right: 0;
    font-family: "Antonio", sans-serif;
    font-weight: 600;
    font-size: 30px;
    line-height: 1;
    letter-spacing: 1.5px;
    text-transform: uppercase;
    color: var(--brand-blue);
  }
  .flavour-name {
    position: absolute;
    top: 170px;
    left: 0;
    width: 196px;
    height: 90px;
  }
  .flavour-name text {
    font-family: "Antonio", sans-serif;
    font-weight: 400;
    font-size: 96px;
    text-transform: uppercase;
  }
  .stop-light { stop-color: var(--accent-light); }
  .stop-dark { stop-color: var(--accent-dark); }
  .tagline {
    position: absolute;
    top: 262px;
    left: 0;
    right: 0;
    font-family: "Pathway Gothic One", sans-serif;
    font-size: 25px;
    line-height: 1.1;
    color: var(--text-white);
  }
  .dot-field {
    position: absolute;
    left: 0;
    right: 0;
    bottom: 0;
    height: 215px;
    background:
      radial-gradient(ellipse at 80% 70%, var(--accent-dark) 0%, transparent 60%),
      radial-gradient(ellipse at 20% 85%, var(--accent-light) 0%, transparent 55%);
    opacity: 0.75;
  }
</style>
</head>
<body>
  <main class="range">
    <section class="label label--tobacco">
      <p class="brand-name">Lumen Drift</p>
      <h2 class="flavour-name">
        <svg width="196" height="90" viewBox="0 0 196 90" aria-label="Tobacco">
          <defs>
            <linearGradient id="grad-tobacco" x1="0" x2="1" y1="0" y2="0">
              <stop offset="0" class="stop-light"/><stop offset="0.55" class="stop-dark"/><stop offset="1" class="stop-light"/>
            </linearGradient>
          </defs>
          <text x="13" y="84" textLength="170" lengthAdjust="spacingAndGlyphs" fill="url(#grad-tobacco)">TOBACCO</text>
        </svg>
      </h2>
      <p class="tagline">Premium Eliquids</p>
      <div class="dot-field" role="img" aria-label="Orange halftone dot pattern"></div>
    </section>
    <section class="label label--fruity">
      <p class="brand-name">Lumen Drift</p>
      <h2 class="flavour-name">
        <svg width="196" height="90" viewBox="0 0 196 90" aria-label="Fruity">
          <defs>
            <linearGradient id="grad-fruity" x1="0" x2="1" y1="0" y2="0">
              <stop offset="0" class="stop-light"/><stop offset="0.55" class="stop-dark"/><stop offset="1" class="stop-light"/>
            </linearGradient>
          </defs>
          <text x="31" y="80" textLength="134" lengthAdjust="spacingAndGlyphs" fill="url(#grad-fruity)">FRUITY</text>
        </svg>
      </h2>
      <p class="tagline">Premium Eliquids</p>
      <div class="dot-field" role="img" aria-label="Coral pink halftone dot pattern"></div>
    </section>
    <section class="label label--minty">
      <p class="brand-name">Lumen Drift</p>
      <h2 class="flavour-name">
        <svg width="196" height="90" viewBox="0 0 196 90" aria-label="Minty">
          <defs>
            <linearGradient id="grad-minty" x1="0" x2="1" y1="0" y2="0">
              <stop offset="0" class="stop-light"/><stop offset="0.55" class="stop-dark"/><stop offset="1" class="stop-light"/>
            </linearGradient>
          </defs>
          <text x="34" y="84" textLength="128" lengthAdjust="spacingAndGlyphs" fill="url(#grad-minty)">MINTY</text>
        </svg>
      </h2>
      <p class="tagline">Premium Eliquids</p>
      <div class="dot-field" role="img" aria-label="Green halftone dot pattern"></div>
    </section>
    <section class="label label--creamy">
      <p class="brand-name">Lumen Drift</p>
      <h2 class="flavour-name">
        <svg width="196" height="90" viewBox="0 0 196 90" aria-label="Creamy">
          <defs>
            <linearGradient id="grad-creamy" x1="0" x2="1" y1="0" y2="0">
              <stop offset="0" class="stop-light"/><stop offset="0.55" class="stop-dark"/><stop offset="1" class="stop-light"/>
            </linearGradient>
          </defs>
          <text x="22" y="80" textLength="152" lengthAdjust="spacingAndGlyphs" fill="url(#grad-creamy)">CREAMY</text>
        </svg>
      </h2>
      <p class="tagline">Premium Eliquids</p>
      <div class="dot-field" role="img" aria-label="Cream halftone dot pattern"></div>
    </section>
  </main>
</body>
</html>
```